Veterinary Business cards

Redesign Business Card

Information needed on Card:
Hours: Mon-Fri: 4pm -10PM; Sat- Sun- 10 AM- 5PM
Help@bayfernvet.com
www.bayfernvet.com
555-718-2946
4173 SE 19th Ave. okc, ok 73958
*No appointment necessary*

Optional:
Our tag line is "We're here when you need us" - If it fits on the cards.

```html
<!DOCTYPE html>
<html lang="en">
<head>
<meta charset="utf-8">
<title>Bayfern Vet Urgent Care – Business Cards</title>
<link rel="stylesheet" href="https://fonts.googleapis.com/css2?family=Lato:wght@400;700&display=swap">
<style>
  :root {
    --backdrop: #232928;
    --cream: #f6efe5;
    --taupe: #a7887a;
    --apricot: #e6ad72;
    --plum-grey: #6e626c;
    --navy: #1f3b6b;
    --orange: #d9822b;
  }
  * { box-sizing: border-box; margin: 0; padding: 0; }
  html, body {
    width: 1200px; height: 800px; overflow: hidden;
    background: var(--backdrop);
    font-family: "Lato", sans-serif;
  }
  .sheet {
    width: 1200px; height: 800px;
    display: flex; align-items: center; justify-content: center; gap: 60px;
  }
  .card {
    position: relative;
    width: 520px; height: 298px;
    border-radius: 28px; overflow: hidden;
    box-shadow: 0 18px 40px rgba(0,0,0,.45);
  }
  .card-shapes { position: absolute; inset: 0; width: 100%; height: 100%; }
  .card-content { position: absolute; inset: 0; color: var(--navy); }

  .brand {
    display: flex; align-items: center; gap: 10px;
    color: var(--navy);
  }
  .brand-dot {
    width: 14px; height: 14px; border-radius: 50%;
    background: var(--orange); flex: none;
  }
  .brand-name {
    font-size: 25px; font-weight: 400; letter-spacing: 1.5px;
    text-transform: uppercase; line-height: 1.15;
  }

  /* Front */
  .card--front .brand { position: absolute; left: 115px; top: 92px; }
  .taglines { position: absolute; left: 128px; top: 170px; }
  .tagline { font-size: 16px; letter-spacing: .6px; margin-bottom: 12px; }
  .tagline--primary { color: var(--orange); }
  .tagline--secondary { color: var(--navy); padding-left: 26px; }

  /* Back */
  .card--back .brand { position: absolute; left: 95px; top: 40px; }
  .card--back .brand-name { font-size: 23px; }
  .hours {
    position: absolute; left: 98px; top: 102px;
    font-size: 11.5px; letter-spacing: .1px; white-space: nowrap;
  }
  .contact-list { position: absolute; left: 112px; top: 142px; list-style: none; }
  .contact-item {
    display: flex; align-items: center; gap: 14px;
    font-size: 13.5px; margin-bottom: 12px;
  }
  .contact-icon { width: 14px; height: 14px; flex: none; fill: none; stroke: var(--navy); stroke-width: 1.6; }
  .contact-icon--solid { fill: var(--navy); stroke: none; }
</style>
</head>
<body>
<main class="sheet">

  <section class="card card--front" aria-label="Card front">
    <svg class="card-shapes" viewBox="0 0 520 298" preserveAspectRatio="none" aria-hidden="true">
      <rect width="520" height="298" fill="var(--taupe)"/>
      <path d="M92 0 Q22 150 72 298 L520 298 L520 0 Z" fill="var(--apricot)"/>
      <path d="M112 0 Q44 150 104 298 L520 298 L520 0 Z" fill="var(--cream)"/>
      <path d="M372 0 Q452 150 318 298 L520 298 L520 0 Z" fill="var(--apricot)"/>
      <path d="M400 0 Q478 150 340 298 L520 298 L520 0 Z" fill="var(--plum-grey)"/>
    </svg>
    <div class="card-content">
      <div class="brand">
        <span class="brand-dot"></span>
        <span class="brand-name">Bayfern Vet<br>Urgent Care</span>
      </div>
      <div class="taglines">
        <p class="tagline tagline--primary">We're here when you need us</p>
        <p class="tagline tagline--secondary">No appointment necessary</p>
      </div>
    </div>
  </section>

  <section class="card card--back" aria-label="Card back">
    <svg class="card-shapes" viewBox="0 0 520 298" preserveAspectRatio="none" aria-hidden="true">
      <rect width="520" height="298" fill="var(--taupe)"/>
      <path d="M80 0 Q14 150 66 298 L520 298 L520 0 Z" fill="var(--apricot)"/>
      <path d="M98 0 Q36 150 94 298 L520 298 L520 0 Z" fill="var(--cream)"/>
      <path d="M385 0 Q462 150 350 298 L520 298 L520 0 Z" fill="var(--apricot)"/>
      <path d="M414 0 Q480 150 370 298 L520 298 L520 0 Z" fill="var(--plum-grey)"/>
      <path d="M434 0 Q494 150 386 298 L520 298 L520 0 Z" fill="var(--taupe)"/>
    </svg>
    <div class="card-content">
      <div class="brand">
        <span class="brand-dot"></span>
        <span class="brand-name">Bayfern Vet<br>Urgent Care</span>
      </div>
      <p class="hours">Hours: Mon-Fri: 4pm -10PM; Sat- Sun- 10 AM- 5PM</p>
      <ul class="contact-list">
        <li class="contact-item">
          <svg class="contact-icon contact-icon--solid" viewBox="0 0 16 16" aria-hidden="true"><path d="M3 1h3l1.5 4-2 1.3a9 9 0 0 0 4.2 4.2L11 8.5l4 1.5v3a2 2 0 0 1-2 2A12 12 0 0 1 1 3a2 2 0 0 1 2-2z"/></svg>
          <span>555-718-2946</span>
        </li>
        <li class="contact-item">
          <svg class="contact-icon" viewBox="0 0 16 16" aria-hidden="true"><path d="M2 8 8 2l6 6M4 7v7h8V7"/></svg>
          <span>4173 SE 19th Ave. okc, ok 73958</span>
        </li>
        <li class="contact-item">
          <svg class="contact-icon contact-icon--solid" viewBox="0 0 16 16" aria-hidden="true"><path d="M1 3h14v10H1z M1 3l7 6 7-6" /></svg>
          <span>Help@bayfernvet.com</span>
        </li>
        <li class="contact-item">
          <svg class="contact-icon" viewBox="0 0 16 16" aria-hidden="true"><circle cx="8" cy="8" r="6.5"/><path d="M1.5 8h13M8 1.5c-3 3.5-3 9.5 0 13M8 1.5c3 3.5 3 9.5 0 13"/></svg>
          <span>www.bayfernvet.com</span>
        </li>
      </ul>
    </div>
  </section>

</main>
</body>
</html>
```